Visitenkartenvorlage ändern
Zielgruppe
Eventmanagement
Aufgabenstellung
Die beiliegende Visitenkarte wäre das "perfekte" Logo für mich. Da es sich hierbei aber um eine Vorlage eines Online-Druck-Anbieters handelt, darf es leider nur für deren Drucke verwendet werden und nicht für Printwerbung, Homepage etc. Daher sollte es genügend verfremdet werden, so dass ich es verwenden kann.

```html
<!DOCTYPE html>
<html lang="de">
<head>
<meta charset="utf-8">
<title>Bella Riva – Visitenkarte</title>
<link rel="stylesheet" href="https://fonts.googleapis.com/css2?family=Open+Sans:wght@400;600&family=Great+Vibes&display=swap">
<style>
  :root {
    --backdrop: #2b2c2e;
    --card: #ecebe9;
    --card-shade: #e3e2e0;
    --ink: #555557;
    --ink-soft: #6a6a6c;
    --accent: #a54a93;
    --flourish: #8e8e90;
    --pattern: #f4f3f2;
  }
  * { box-sizing: border-box; margin: 0; padding: 0; }
  html, body {
    width: 1163px;
    height: 1200px;
    overflow: hidden;
    background: var(--backdrop);
  }
  body { position: relative; font-family: "Open Sans", Arial, sans-serif; color: var(--ink); }

  .card {
    position: absolute;
    left: 227px;
    width: 707px;
    height: 406px;
    background: var(--card);
  }
  .card--front { top: 178px; }
  .card--back  { top: 673px; }

  .brand-name {
    position: absolute;
    left: 0; right: 0;
    text-align: center;
    font-size: 27px;
    font-weight: 400;
    letter-spacing: 0.2em;
    color: var(--ink);
    line-height: 1;
  }
  .tagline {
    position: absolute;
    left: 0; right: 0;
    text-align: center;
    font-size: 18px;
    font-variant: small-caps;
    letter-spacing: 0.14em;
    color: var(--ink);
    line-height: 1;
  }
  .web {
    position: absolute;
    left: 0; right: 0;
    text-align: center;
    font-size: 15px;
    letter-spacing: 0.04em;
    color: var(--ink);
    line-height: 1;
  }
  .brand-mark {
    position: absolute;
    left: 50%;
    border-radius: 50%;
    background: var(--accent);
    transform: translateX(-50%);
  }

  .card--front .brand-name { top: 76px; }
  .card--front .brand-mark { top: 180px; width: 54px; height: 54px; }
  .card--front .tagline    { top: 298px; }
  .card--front .web        { top: 332px; }

  .back-pattern {
    position: absolute;
    left: 0; right: 0;
    top: 96px; bottom: 0;
    background: linear-gradient(180deg, var(--pattern), var(--card-shade));
  }
  .flourish-band {
    position: absolute;
    left: 12px; right: 12px;
    top: 84px;
    height: 12px;
    background: linear-gradient(90deg, transparent, var(--flourish) 12%, var(--flourish) 42%, transparent 50%, var(--flourish) 58%, var(--flourish) 88%, transparent);
    opacity: 0.45;
    border-radius: 6px;
  }
  .card--back .brand-mark { top: 30px; width: 38px; height: 38px; }
  .card--back .brand-name { top: 143px; }
  .card--back .tagline    { top: 194px; }
  .person-name {
    position: absolute;
    left: 0; right: 0;
    top: 246px;
    text-align: center;
    font-family: "Great Vibes", cursive;
    font-size: 36px;
    color: var(--accent);
    line-height: 1;
  }
  .contact {
    position: absolute;
    top: 350px;
    font-size: 16px;
    letter-spacing: 0.14em;
    color: var(--ink-soft);
    line-height: 1;
  }
  .contact--email { left: 60px; font-variant: small-caps; }
  .contact--phone { right: 55px; letter-spacing: 0.06em; font-size: 17px; }
</style>
</head>
<body>
  <section class="card card--front" aria-label="Vorderseite">
    <h1 class="brand-name">BELLA RIVA</h1>
    <div class="brand-mark" aria-hidden="true"></div>
    <p class="tagline">Events und mehr</p>
    <p class="web">WWW.BELLA-RIVA.DE</p>
  </section>

  <section class="card card--back" aria-label="Rückseite">
    <div class="back-pattern" role="img" aria-label="Zartes florales Hintergrundmuster"></div>
    <div class="flourish-band" role="img" aria-label="Ornamentale Schmuckbordüre"></div>
    <div class="brand-mark" aria-hidden="true"></div>
    <h2 class="brand-name">BELLA RIVA</h2>
    <p class="tagline">Events und mehr</p>
    <p class="person-name">Beluntora Venski</p>
    <p class="contact contact--email">info@bella-riva.de</p>
    <p class="contact contact--phone">+ 49 170&nbsp; 4402718</p>
  </section>
</body>
</html>
```